Heronby Mortgage Capital Business Card

We need a business card design for our mortgage servicing company. In addition to servicing the loans of homeowners, we help homeowners with purchasing their homes and any mortgage refinancing. We would like to see designs that use the colors in the logo attached below (gold-ish yellow and navy blue), and any other design you deem fit! The design should communicate a simpler life with smart mortgages provided by Heronby.

```html
<!DOCTYPE html>
<html lang="en">
<head>
<meta charset="utf-8">
<title>Heronby Mortgage Capital – Business Card</title>
<link rel="stylesheet" href="https://fonts.googleapis.com/css2?family=EB+Garamond:wght@400;600&display=swap">
<style>
  :root {
    --page-bg: #2b2b2c;
    --gold: #d6a63c;
    --gold-light: #e2b443;
    --navy: #232052;
    --rule: #8e8aa8;
    --card-white: #ffffff;
    --card-shade: #e6e6e6;
    --ink-soft: #3a3a4a;
  }
  * { box-sizing: border-box; margin: 0; padding: 0; }
  html, body { width: 1200px; height: 900px; overflow: hidden; }
  body {
    background: var(--page-bg);
    font-family: "EB Garamond", Georgia, serif;
    position: relative;
  }
  .card {
    position: absolute;
    left: 300px;
    width: 600px;
    height: 343px;
    border-radius: 30px;
    overflow: hidden;
    box-shadow: 0 14px 30px rgba(0,0,0,0.45);
  }
  .card--front {
    top: 62px;
    background: linear-gradient(100deg, var(--gold) 0%, var(--gold-light) 100%);
  }
  .card--back {
    top: 478px;
    background: linear-gradient(110deg, var(--card-shade) 0%, var(--card-white) 55%, var(--card-white) 100%);
  }
  .wordmark {
    position: absolute;
    display: flex;
    align-items: center;
    gap: 12px;
    color: var(--navy);
    font-weight: 600;
    letter-spacing: 0.5px;
    line-height: 1;
  }
  .wordmark__dot {
    width: 14px; height: 14px; border-radius: 50%;
    background: var(--navy);
  }
  .card--front .wordmark {
    left: 50%;
    top: 140px;
    transform: translateX(-50%);
    font-size: 50px;
  }
  .front-rule {
    position: absolute;
    left: 110px; right: 70px; top: 222px;
    height: 1px;
    background: var(--rule);
  }
  .front-web {
    position: absolute;
    left: 0; right: 0; top: 236px;
    text-align: center;
    font-size: 17px;
    color: var(--navy);
    letter-spacing: 0.5px;
  }
  .card--back .wordmark {
    left: 48px;
    top: 62px;
    font-size: 46px;
  }
  .contact {
    position: absolute;
    left: 48px; right: 44px; bottom: 40px;
    color: var(--ink-soft);
    font-size: 15px;
  }
  .contact__name-row {
    display: flex;
    align-items: baseline;
    gap: 8px;
    margin-bottom: 6px;
  }
  .contact__name {
    color: var(--gold);
    font-size: 19px;
    letter-spacing: 1px;
    text-transform: uppercase;
  }
  .contact__sep { color: var(--gold); }
  .contact__title { font-size: 17px; }
  .contact__rule-row {
    display: flex;
    align-items: center;
    gap: 10px;
  }
  .contact__rule-row .rule {
    flex: 1;
    height: 1px;
    background: var(--rule);
  }
  .contact__line { line-height: 1.45; white-space: nowrap; }
  .label { color: var(--gold); margin-right: 4px; }
</style>
</head>
<body>

  <section class="card card--front" aria-label="Business card front">
    <div class="wordmark"><span class="wordmark__dot"></span>Heronby</div>
    <div class="front-rule"></div>
    <p class="front-web">www.heronbymortgage.com</p>
  </section>

  <section class="card card--back" aria-label="Business card back">
    <div class="wordmark"><span class="wordmark__dot"></span>Heronby</div>
    <div class="contact">
      <div class="contact__name-row">
        <span class="contact__name">Owen Hartley</span>
        <span class="contact__sep">|</span>
        <span class="contact__title">Director</span>
      </div>
      <div class="contact__rule-row contact__line">
        <span><span class="label">P.</span>300-555-0142</span>
        <span class="rule"></span>
      </div>
      <p class="contact__line">
        <span class="label">E.</span>info@heronbymortgage.com
        <span class="contact__sep"> | </span>www.heronbymortgage.com
        <span class="contact__sep"> | </span>12 harbor lane, bayford 0000
      </p>
    </div>
  </section>

</body>
</html>
```